3D Geology Modelling Web Design Project

I am a consultant who carries out 3D computer modelling for the mining and exploration industry. I am looking for a fully funcitonal corporate looking website for a small business and my logo is hosted at www.tarvolo.com.au. I will need around 7 pages or so (a description and sitemap are in a document called Tarvolo Website_brief.pdf , this document along with pictures and logo can be found at http://www.tarvolo.com.au/tarvolopics). The pages will be mostly static with some simple flash transitions and a simple enquiry form on a contact page. Otherwise just text and pics +/- flash. I will want to be able to update the pages myself, so what options are available for doing this (e.g. wordpress?). I also want it cross-browser and cross-platform friendly e.g. xhtml?

Similar style websites are:

http://www.pebblindrift.com.au/
http://www.ryvquarrying.com.au/
http://www.prismvale.com/Default.aspx
http://www.nolbeworld.com/
http://www.tuv.com/en
http://www.lodpfa.com/

Please have a look at the above samples to get a feel for what I am after. It’s a relatively simple standing site and I would want it done in a colour scheme that matches my logo which is blue and silver. I already have the domain name and hosting setup.

regards, Peter

Reason: Hi Everyone, I am extending the deadline for the final time just to give interested parties enough time to submit revisions. I will be choosing the final design on this deadline. Thanks, Peter

Target Market(s)

Geologists and Mining Companies varied ages male and female from 21-65 yo

Industry/Entity Type

Small Business

Requirements
Must have
• Cross platform and cross browser functionality e.g. can be seen in different browsers and on mobiles etc.. wirtten in xhtml?
Search Engine optimisation. LinkedIn connection?
Nice to have
• Some simple blending of header pictures with logo to give it a nice flow, rather than sharp discrete images. Some artistic licence is welcomed. Some flash style in banner? I have a lot of images and backgrounds to choose from now located on my website.

www.tarvolo.com/tarvolopics
Should not have
• No sounds

```html
<!DOCTYPE html>
<html lang="en">
<head>
<meta charset="utf-8">
<title>Tarvolo – Geoscience Modelling Consultants</title>
<link rel="stylesheet" href="https://fonts.googleapis.com/css2?family=Open+Sans:ital,wght@0,400;0,600;0,700;1,600;1,700&family=Arimo:wght@400;700&family=Oswald:wght@500;700&family=PT+Sans+Narrow:wght@700&display=swap">
<style>
:root{
  --sand:#e9dcc6;
  --sand-dark:#dccbb0;
  --page:#ffffff;
  --blue:#0a6fbe;
  --blue-dark:#0b5296;
  --blue-light:#2f97e0;
  --ink:#1e1e1e;
  --body:#333333;
  --card:#f6f6f6;
  --news:#7d7462;
  --footer-top:#9e9e9e;
  --footer-bot:#cfcfcf;
}
*{margin:0;padding:0;box-sizing:border-box}
html,body{width:758px;height:1200px;overflow:hidden}
body{background:radial-gradient(circle at 30% 20%,var(--sand) 0%,var(--sand-dark) 100%);font-family:"Open Sans",sans-serif;color:var(--body);position:relative}
.abs{position:absolute}
.page{left:50px;top:0;width:660px;height:1191px;background:var(--page);box-shadow:0 0 4px rgba(0,0,0,.25)}
.brand{left:62px;top:18px}
.brand-name{font-family:"Arimo",sans-serif;font-weight:700;font-size:46px;color:var(--blue);letter-spacing:1px;line-height:46px;display:flex;align-items:center;gap:10px}
.brand-mark{width:40px;height:40px;border-radius:50%;background:var(--blue)}
.brand-tag{font-family:"Arimo",sans-serif;font-size:9.5px;color:#6a6a6a;margin-top:4px;letter-spacing:.2px}
.social{display:flex;gap:8px}
.social span{width:21px;height:21px;border-radius:50%;background:radial-gradient(circle at 35% 30%,var(--blue-light),var(--blue-dark))}
.top-social{left:613px;top:23px}
.search{left:550px;top:60px;width:144px;height:24px;background:#efefef;border:1px solid #dcdcdc;font-size:8.5px;color:#555;padding:5px 8px}
.search-btn{right:0;top:0;width:25px;height:22px;background:var(--blue)}
.nav{left:39px;top:110px;width:683px;height:30px;background:linear-gradient(var(--blue-light),var(--blue-dark));display:flex;font-size:9px;color:#fff}
.nav a{color:#fff;text-decoration:none;display:flex;align-items:center;justify-content:center;height:100%}
.nav .active{background:linear-gradient(#5ab5ee,#2f97e0)}
.fold{width:0;height:0;border-top:9px solid #1e2a36}
.fold-l{left:39px;top:140px;border-left:11px solid transparent}
.fold-r{left:711px;top:140px;border-right:11px solid transparent}
.slider{left:64px;top:148px;width:632px;height:261px;border:1px solid #ddd;background:#fff;box-shadow:0 6px 8px -4px rgba(0,0,0,.3)}
.slide-img{left:3px;top:3px;width:624px;height:254px;background:linear-gradient(180deg,#aab4bd 0%,#8d9aa3 22%,#6e7f47 34%,#a4865a 55%,#8b6a48 78%,#b89a74 100%)}
.slide-title{left:30px;top:152px;font-family:"Oswald",sans-serif;font-weight:700;font-size:29px;line-height:37px;color:#1a1a1a;-webkit-text-stroke:.6px #fff;text-shadow:0 0 2px #fff,1px 1px 0 #fff}
.arrow{width:18px;height:19px;background:var(--blue);display:flex;align-items:center;justify-content:center}
.pager{left:256px;top:234px;width:120px;height:23px;background:var(--blue-dark);clip-path:polygon(8% 0,92% 0,100% 100%,0 100%);display:flex;gap:5px;align-items:center;justify-content:center;padding-top:2px}
.pager i{width:9px;height:9px;border-radius:50%;background:#fff;display:block}
.pager i:first-child{background:#222}
.welcome{left:70px;top:432px;font-family:"Arimo",sans-serif;font-weight:400;font-size:11.5px;color:#333}
.welcome b{font-weight:400;font-size:15.5px;color:var(--blue)}
.intro{left:70px;top:457px;width:392px;font-size:8.3px;line-height:11.3px;color:var(--ink)}
.sub{font-family:"Arimo",sans-serif;font-weight:400;font-size:9.5px;color:var(--blue)}
.item{font-size:8.2px;font-style:italic;font-weight:600;color:#222}
.more{font-size:7.5px;color:var(--blue)}
.news-pill{left:488px;top:432px;width:200px;height:34px;border-radius:17px;background:linear-gradient(#a39a86,var(--news));box-shadow:0 2px 3px rgba(0,0,0,.3);font-family:"Oswald",sans-serif;font-size:14px;color:#fff;padding:7px 0 0 52px}
.news-icon{left:10px;top:4px;width:28px;height:25px;border-radius:4px;background:#e4c97a}
.news-t{font-size:8.3px;font-weight:700;color:var(--blue)}
.news-p{width:190px;font-size:8.3px;line-height:11px;color:#333}
.services{left:64px;top:671px;width:632px;height:224px;background:linear-gradient(#f7f7f7,#e2e2e2)}
.services-head{left:0;top:10px;width:632px;text-align:center;font-family:"PT Sans Narrow",sans-serif;font-size:11.5px;color:#444}
.services-head::before,.services-head::after{content:"";position:absolute;top:7px;width:270px;border-top:3px double #c8c8c8}
.services-head::before{left:0}.services-head::after{right:0}
.card{width:173px;height:160px;background:var(--card);border:1px solid #e2e2e2;top:41px;box-shadow:0 6px 6px -5px rgba(0,0,0,.35)}
.card h3{height:31px;border-bottom:1px solid #ddd;background:#eee;font-family:"PT Sans Narrow",sans-serif;font-size:11px;color:#222;text-align:center;line-height:31px}
.card-img{left:8px;top:41px;width:157px;height:62px}
.card p{position:absolute;left:9px;top:118px;width:158px;font-size:8px;line-height:11px;color:#333}
.card .more{position:absolute;left:9px;top:144px}
.clients-title{left:70px;top:912px;font-family:"Arimo",sans-serif;font-weight:400;font-size:12px;color:var(--blue)}
.clients{left:65px;top:939px;width:631px;height:86px;background:#fff;box-shadow:0 0 8px rgba(0,0,0,.18)}
.client{top:0;height:86px;display:flex;align-items:center;gap:5px;font-size:10px;font-weight:700;color:#555;transform:translateX(-50%);white-space:nowrap}
.client i{width:10px;height:10px;background:#8a8a8a;display:block}
.arrow-dark{background:#111;width:18px;height:19px;display:flex;align-items:center;justify-content:center}
.footer{left:64px;top:1056px;width:633px;height:121px;background:linear-gradient(var(--footer-bot),var(--footer-top) 55%,#bdbdbd)}
.f-addr{left:9px;top:15px;font-size:8.3px;line-height:16px;color:#111}
.f-map{left:215px;top:14px;width:225px;height:66px;border:2px solid #555;background:linear-gradient(135deg,#b9d3ea,#e9dfc0 45%,#d8cfae 70%,#b9d3ea)}
.f-touch{left:505px;top:15px;width:84px;text-align:center;font-size:8.3px;color:#111}
.f-social{left:505px;top:38px}
.f-line{left:8px;top:90px;width:617px;border-top:1px solid #c7c7c7}
.f-bottom{top:100px;font-size:7.3px;color:#111}
</style>
</head>
<body>
<div class="abs page"></div>

<header>
  <div class="abs brand">
    <div class="brand-name">TARVOLO <span class="brand-mark"></span></div>
    <div class="brand-tag">GEOSCIENCE MODELLING CONSULTANTS</div>
  </div>
  <div class="abs social top-social" aria-label="Social links"><span></span><span></span><span></span></div>
  <div class="abs search">Search
    <span class="abs search-btn"><svg width="25" height="22" viewBox="0 0 25 22"><circle cx="14" cy="9" r="4.5" fill="none" stroke="#fff" stroke-width="1.6"/><line x1="10.8" y1="12.2" x2="7" y2="16" stroke="#fff" stroke-width="2"/></svg></span>
  </div>
  <nav class="abs nav">
    <a class="active" style="width:91px">HOME</a>
    <a style="width:88px">ABOUT</a>
    <a style="width:96px">SERVICES</a>
    <a style="width:88px">CLIENTS</a>
    <a style="width:118px">PUBLICATIONS</a>
    <a style="width:98px">TRAINING</a>
    <a style="width:104px">CONTACT</a>
  </nav>
  <div class="abs fold fold-l"></div><div class="abs fold fold-r"></div>
</header>

<section class="abs slider">
  <div class="abs slide-img" role="img" aria-label="Open-pit mine with layered rock walls under a cloudy sky"></div>
  <h1 class="abs slide-title">GEOLOGY AND GEOLOGICAL<br>MODELLING CONSULTANCY</h1>
  <div class="abs arrow" style="left:3px;top:123px"><svg width="8" height="10"><path d="M6 1L2 5l4 4" stroke="#fff" stroke-width="2" fill="none"/></svg></div>
  <div class="abs arrow" style="left:609px;top:123px"><svg width="8" height="10"><path d="M2 1l4 4-4 4" stroke="#fff" stroke-width="2" fill="none"/></svg></div>
  <div class="abs pager"><i></i><i></i><i></i><i></i><i></i><i></i></div>
</section>

<main>
  <h2 class="abs welcome">welcome to <b>TARVOLO- Geoscience Modelling Consultants</b></h2>
  <p class="abs intro">Lorem ipsum dolor sit amet, consectetur adipiscing elit. Morbi pharetra auctor gravida. Quisque male suada nisi sit amet lacus auctor cursus. Phasellus consectetur adipiscing lectus vel egestas. Aenean ut elit sit amet leo dapibus cursus et fringilla magna. Phasellus placerat tellus nec dui interdum lacinia. Nam pellentesque condimentum vehicula. Fusce mattis arcu ligula.</p>
  <h3 class="abs sub" style="left:70px;top:514px">Specialising In</h3>
  <p class="abs item" style="left:70px;top:536px">1. Structural and Geomechanical Analysis of Hydrothermal Systems</p>
  <p class="abs item" style="left:70px;top:552px">2. Prospectivity Analysis and Target Generation</p>
  <h3 class="abs sub" style="left:70px;top:579px">Specialisit Techniques</h3>
  <p class="abs item" style="left:70px;top:598px">1. Structural Geology and Remote Sensed Data Interpretation</p>
  <p class="abs item" style="left:70px;top:614px">2. Geomechanical Modelling of both Continuous and discrete Geological Processes</p>
  <a class="abs more" style="left:70px;top:638px">» Read More</a>

  <aside>
    <div class="abs news-pill"><span class="abs news-icon" role="img" aria-label="Newspaper icon"></span>LATEST NEWS</div>
    <h4 class="abs news-t" style="left:493px;top:475px">Lorem ipsum dolor site maer</h4>
    <p class="abs news-p" style="left:493px;top:491px">We have a new website! What do you think? We can upload sermons for you to listen.</p>
    <h4 class="abs news-t" style="left:493px;top:528px">Lorem ipsum dolor site maer</h4>
    <p class="abs news-p" style="left:493px;top:544px">We have a new website! What do you think? We can upload sermons .</p>
    <h4 class="abs news-t" style="left:493px;top:583px">Lorem ipsum dolor site maer</h4>
    <p class="abs news-p" style="left:493px;top:599px">We have a new website! What do you think? We can upload sermons for you to listen.</p>
    <a class="abs more" style="left:493px;top:638px">» Read More</a>
  </aside>

  <section class="abs services">
    <h2 class="abs services-head">OUR SERVICES</h2>
    <div class="abs card" style="left:11px">
      <h3>STRUCTURAL ANALYSIS</h3>
      <div class="abs card-img" role="img" aria-label="Consultants reviewing work at a desk in an office" style="background:linear-gradient(135deg,#c9d6e2,#6f7f8e 60%,#2f3338)"></div>
      <p>Lorem ipsum dolor sit maer seta di mari a nuno valencia est do dummy text</p>
      <a class="more">» Read More</a>
    </div>
    <div class="abs card" style="left:230px">
      <h3>GEOMECHANICAL ANALYSIS</h3>
      <div class="abs card-img" role="img" aria-label="Close-up of layered rock face" style="background:linear-gradient(135deg,#c58a45,#7a4a22 55%,#d3ae7a)"></div>
      <p>Lorem ipsum dolor sit maer seta di mari a nuno valencia est do dummy text</p>
      <a class="more">» Read More</a>
    </div>
    <div class="abs card" style="left:449px">
      <h3>PROSPECTIVITY ANALYSIS</h3>
      <div class="abs card-img" role="img" aria-label="Underground mine tunnel lit in orange" style="background:linear-gradient(90deg,#a9471a,#3e2418 50%,#7a6a66)"></div>
      <p>Lorem ipsum dolor sit maer seta di mari a nuno valencia est do dummy text</p>
      <a class="more">» Read More</a>
    </div>
  </section>

  <h2 class="abs clients-title">Our Clients</h2>
  <section class="abs clients">
    <div class="abs arrow-dark" style="left:0;top:35px"><svg width="8" height="10"><path d="M6 1L2 5l4 4" stroke="#fff" stroke-width="2" fill="none"/></svg></div>
    <div class="abs client" style="left:82px"><i></i>Korrand</div>
    <div class="abs client" style="left:166px"><i></i>Velmora</div>
    <div class="abs client" style="left:258px"><i></i>Quellix</div>
    <div class="abs client" style="left:346px"><i></i>Brevanta</div>
    <div class="abs client" style="left:420px"><i></i>Ostrel</div>
    <div class="abs client" style="left:495px"><i></i>Harlow</div>
    <div class="abs client" style="left:573px"><i></i>Dunmere</div>
    <div class="abs arrow-dark" style="left:613px;top:35px"><svg width="8" height="10"><path d="M2 1l4 4-4 4" stroke="#fff" stroke-width="2" fill="none"/></svg></div>
  </section>
</main>

<footer class="abs footer">
  <p class="abs f-addr">Tarvolo Geoscience Consulting<br>Fenwick Road, Ashbury, AB4 7QT<br>Email: hello@tarvolo.com<br>Phone: 01632 960418</p>
  <div class="abs f-map" role="img" aria-label="Map of the office location"></div>
  <p class="abs f-touch">Get In Touch With Us</p>
  <div class="abs social f-social" style="gap:13px;left:505px"><span></span><span></span><span></span></div>
  <div class="abs f-line"></div>
  <p class="abs f-bottom" style="left:19px">© 2013, All Rights Reserved</p>
  <p class="abs f-bottom" style="left:245px">Terms &amp; Conditions &nbsp;|&nbsp; Privacy &nbsp;|&nbsp; Help</p>
  <p class="abs f-bottom" style="left:487px">Design &amp; Developed By: Quorrin Studio</p>
</footer>
</body>
</html>
```